Business Card Design Project

I want my business cards to stand and feel timeless! I also want people to get their hands on them and freak out over how cool these are, I already have a logo i just want a very cool card design! this is for a makeup artist and maybe one day a line of cosmetics.

Target Market(s)

I want this to target women from 18 to 45

Industry/Entity Type

Business

Font styles to use
Decorative
Script

Colors

Designer to choose colors to be used in the design.

Requirements
Must have
• it must be elegante

```html
<!DOCTYPE html>
<html lang="en">
<head>
<meta charset="utf-8">
<title>Studio Rosalie — Business Cards</title>
<link rel="stylesheet" href="https://fonts.googleapis.com/css2?family=Montserrat:wght@300;400;500&display=swap">
<style>
  :root {
    --bg: #ece8e4;
    --card: #ffffff;
    --ink: #1f1f1f;
    --ink-soft: #333333;
    --magenta: #d0368c;
    --peach-line: #e9a38c;
    --photo-a: #f6d6d2;
    --photo-b: #eaa39c;
    --photo-c: #f3e6dc;
    --shadow: rgba(60, 40, 30, 0.18);
  }
  * { box-sizing: border-box; margin: 0; padding: 0; }
  html, body {
    width: 1200px; height: 848px; overflow: hidden;
    background: var(--bg);
    font-family: "Montserrat", Arial, sans-serif;
    color: var(--ink);
  }
  .sheet {
    width: 1200px; height: 848px;
    display: flex; align-items: center; justify-content: center; gap: 40px;
  }
  .card {
    position: relative;
    width: 560px; height: 320px;
    background: var(--card);
    box-shadow: 0 10px 30px var(--shadow);
  }
  .wordmark {
    font-weight: 300;
    color: var(--ink);
    letter-spacing: 0.14em;
    text-transform: uppercase;
    white-space: nowrap;
  }
  .photo-area {
    position: absolute;
    background: linear-gradient(120deg, var(--photo-c) 0%, var(--photo-a) 45%, var(--photo-b) 100%);
  }

  /* Front: contact side */
  .card--front .person { position: absolute; left: 26px; top: 42px; }
  .person__name { font-size: 25px; font-weight: 400; color: var(--magenta); line-height: 1.05; }
  .person__role { font-size: 23px; font-weight: 400; color: var(--ink); line-height: 1.1; }
  .card--front .wordmark { position: absolute; right: 40px; top: 30px; font-size: 24px; }
  .card--front .divider {
    position: absolute; left: 300px; top: 118px; width: 1px; height: 110px;
    background: linear-gradient(var(--peach-line), rgba(233,163,140,0.2));
  }
  .card--front .photo-area { left: 96px; top: 196px; width: 190px; height: 106px; }
  .contact {
    position: absolute; right: 24px; top: 128px;
    list-style: none; text-align: right;
    font-size: 13px; line-height: 20px; color: var(--ink-soft);
  }
  .contact li { display: flex; justify-content: flex-end; align-items: center; gap: 10px; }
  .contact svg { width: 13px; height: 13px; flex: none; }
  .contact .address { align-items: flex-start; }
  .contact .address span { line-height: 17px; }

  /* Back: brand side */
  .card--back .photo-area { right: 56px; top: 26px; width: 230px; height: 112px; }
  .card--back .wordmark {
    position: absolute; left: 0; right: 0; top: 178px;
    text-align: center; font-size: 40px; letter-spacing: 0.16em;
  }
</style>
</head>
<body>
<main class="sheet">

  <section class="card card--front" aria-label="Card front with contact details">
    <div class="person">
      <p class="person__name">Mara Ellison</p>
      <p class="person__role">Make Up Artist</p>
    </div>
    <p class="wordmark">Studio Rosalie</p>
    <div class="divider"></div>
    <div class="photo-area" role="img" aria-label="Beauty portrait with blush and makeup products"></div>
    <ul class="contact">
      <li><span>(555) 218 4093</span>
        <svg viewBox="0 0 12 12" aria-hidden="true"><rect x="3" y="0.5" width="6" height="11" rx="1" fill="none" stroke="#333"/><line x1="5" y1="9.5" x2="7" y2="9.5" stroke="#333"/></svg></li>
      <li><span>mara@ellisonbeauty.com</span>
        <svg viewBox="0 0 12 12" aria-hidden="true"><rect x="0.5" y="2.5" width="11" height="7" fill="#333"/><polyline points="0.5,2.5 6,7 11.5,2.5" fill="none" stroke="#fff"/></svg></li>
      <li><span>www.ellisonbeauty.com</span>
        <svg viewBox="0 0 12 12" aria-hidden="true"><circle cx="6" cy="6" r="5.3" fill="none" stroke="#333"/><ellipse cx="6" cy="6" rx="2.3" ry="5.3" fill="none" stroke="#333"/><line x1="0.7" y1="6" x2="11.3" y2="6" stroke="#333"/></svg></li>
      <li class="address"><span>18 Linden Hollow Lane, 4410,<br>Brookvale</span>
        <svg viewBox="0 0 12 12" aria-hidden="true"><path d="M6 11.5 L2.4 5.6 A4 4 0 1 1 9.6 5.6 Z" fill="#333"/><circle cx="6" cy="4.2" r="1.4" fill="#fff"/></svg></li>
    </ul>
  </section>

  <section class="card card--back" aria-label="Card back with brand name">
    <div class="photo-area" role="img" aria-label="Beauty portrait with blush and makeup products"></div>
    <p class="wordmark">Studio Rosalie</p>
  </section>

</main>
</body>
</html>
```